Financial Planning Firm looking for stationary design using new logo

Need stationary design using our new logo. We are a financial planning firm focused on the planning needs of retirees. Design should incorporate our new logo and its colors. The design should communicate a feeling of stability and security.
Have attached our new logo, as well as our old stationary for reference, letterhead, envelope and business card (but don't rely on for your design). Although the following disclosure must be present on all items "Securities and advisory services offered through Valdimo Advisor Networks LLC, member QUBEX/DLWT. Valdimo is under seperate ownership from any other named entity." in minimum 8 size font. you can see our old stationary for idea of disclosure placement. The business card (front and back) is in the middle of our letterhead sample if it is hard to tell.
Financial

```html
<!DOCTYPE html>
<html lang="en">
<head>
<meta charset="utf-8">
<title>Marlow T. Hale Financial Group — Stationery</title>
<link rel="stylesheet" href="https://fonts.googleapis.com/css2?family=Montserrat:wght@400;600;700&display=swap">
<style>
  :root {
    --navy: #1d4e6f;
    --navy-deep: #164462;
    --charcoal: #4a4a4a;
    --text: #595e63;
    --paper: #ffffff;
    --paper-shade: #f2f3f4;
    --stripe: #c9cccf;
    --backdrop: #d6d8da;
  }
  * { box-sizing: border-box; margin: 0; padding: 0; }
  html, body { width: 1200px; height: 1000px; overflow: hidden; }
  body {
    background: var(--backdrop);
    font-family: "Montserrat", Arial, sans-serif;
    color: var(--text);
    position: relative;
  }
  .sheet {
    position: absolute;
    background: var(--paper);
    box-shadow: 0 2px 6px rgba(0,0,0,.18);
    overflow: hidden;
  }
  .band {
    position: absolute; left: 0; right: 0; bottom: 0;
    height: 8px; background: var(--navy);
    border-top: 3px solid var(--stripe);
    box-sizing: content-box;
  }

  /* brand lockup */
  .brand { display: flex; align-items: center; gap: 6px; }
  .brand-dot {
    border-radius: 50%; background: var(--navy);
    border: 2px solid var(--charcoal); flex: none;
  }
  .brand-name {
    font-weight: 600; color: var(--navy); text-transform: uppercase;
    line-height: 1.05; letter-spacing: .02em;
  }
  .brand-name small { display: block; font-weight: 600; text-transform: none; letter-spacing: .04em; }

  /* letterhead */
  .letterhead { left: 140px; top: 82px; width: 448px; height: 580px; }
  .letterhead .brand { position: absolute; left: 41px; top: 36px; }
  .letterhead .brand-dot { width: 30px; height: 30px; }
  .letterhead .brand-name { font-size: 11px; }
  .letterhead .brand-name small { font-size: 6.5px; }
  .contact { position: absolute; left: 334px; top: 34px; font-size: 5.6px; line-height: 8.4px; }
  .contact li { list-style: none; display: flex; align-items: center; gap: 4px; }
  .contact svg { width: 6px; height: 6px; fill: var(--navy); }
  .contact .addr { margin-bottom: 4px; }
  .letter { position: absolute; left: 41px; top: 100px; width: 370px; font-size: 5.8px; line-height: 7.5px; }
  .letter .date { margin-bottom: 11px; }
  .letter .greeting { font-weight: 700; margin: 53px 0 7px; color: var(--charcoal); }
  .letter p.body { margin-bottom: 7px; text-align: justify; }
  .letter .closing { margin-top: 22px; }
  .letter .closing b { color: var(--charcoal); }
  .signature {
    position: absolute; left: 95px; top: 390px; width: 95px; height: 40px;
    background: linear-gradient(90deg, rgba(52,70,160,.18), rgba(52,70,160,.08));
    border-radius: 3px;
  }
  .fold-mark { position: absolute; left: 0; width: 6px; height: 1px; background: #bbb; }
  .disclosure { position: absolute; font-size: 5.2px; line-height: 6.6px; color: var(--navy); }
  .letterhead .disclosure { left: 41px; bottom: 20px; }

  /* business cards */
  .card { top: 82px; width: 186px; height: 103px; }
  .card .band { height: 4px; border-top-width: 2px; }
  .card .brand { position: absolute; left: 12px; top: 10px; gap: 4px; }
  .card .brand-dot { width: 17px; height: 17px; border-width: 1.5px; }
  .card .brand-name { font-size: 6.4px; }
  .card .brand-name small { font-size: 4px; }
  .card-front { left: 634px; }
  .card-back { left: 867px; }
  .person { position: absolute; right: 12px; top: 50px; text-align: right; font-size: 4px; line-height: 5.6px; }
  .person strong { color: var(--navy); font-size: 5px; }
  .card-line { position: absolute; left: 10px; right: 12px; font-size: 3.4px; text-align: right; white-space: nowrap; }
  .card-back .disclosure { left: 12px; top: 72px; font-size: 4px; line-height: 5px; color: var(--text); }

  /* folder */
  .folder { left: 634px; top: 235px; width: 464px; height: 602px; border-radius: 0 4px 4px 0; }
  .folder-top { position: absolute; left: 0; right: 0; top: 0; height: 236px; background: linear-gradient(#fff, var(--paper-shade)); }
  .folder-stripe { position: absolute; left: 0; right: 0; top: 236px; height: 8px; background: var(--stripe); }
  .folder-bottom { position: absolute; left: 0; right: 0; top: 244px; bottom: 0; background: linear-gradient(180deg, #21587c, var(--navy-deep)); }
  .spine { position: absolute; top: 0; bottom: 0; width: 1px; background: rgba(0,0,0,.12); }
  .folder .brand { position: absolute; left: 134px; top: 74px; gap: 8px; }
  .folder .brand-dot { width: 50px; height: 50px; border-width: 3px; }
  .folder .brand-name { font-size: 17px; }
  .folder .brand-name small { font-size: 10px; }

  /* envelope */
  .envelope { left: 86px; top: 708px; width: 502px; height: 217px; }
  .envelope .brand { position: absolute; left: 21px; top: 22px; }
  .envelope .brand-dot { width: 30px; height: 30px; }
  .envelope .brand-name { font-size: 11px; }
  .envelope .brand-name small { font-size: 6.5px; }
  .return-addr { position: absolute; left: 57px; top: 63px; font-size: 5.8px; line-height: 7.6px; }
</style>
</head>
<body>

<section class="sheet letterhead" aria-label="Letterhead">
  <div class="brand"><span class="brand-dot"></span><span class="brand-name">Marlow T. Hale<br>Financial Group, LLC<small>Steady Ground For Tomorrow</small></span></div>
  <ul class="contact">
    <li class="addr">4820 Harbor Avenue, Suite 310<br>Alder, WA 98110</li>
    <li><svg viewBox="0 0 10 10"><circle cx="5" cy="5" r="5"/></svg>555.214.3380</li>
    <li><svg viewBox="0 0 10 10"><circle cx="5" cy="5" r="5"/></svg>555.214.3391</li>
    <li><svg viewBox="0 0 10 10"><circle cx="5" cy="5" r="5"/></svg>mhale@marlowhale.com</li>
    <li><svg viewBox="0 0 10 10"><circle cx="5" cy="5" r="5"/></svg>www.marlowhale.com</li>
  </ul>
  <span class="fold-mark" style="top:217px"></span>
  <span class="fold-mark" style="top:437px"></span>
  <div class="letter">
    <p class="date">30.02.2015</p>
    <p class="recipient">Recipient's name<br>Lindenweg 14<br>20251 Hamburg<br>Germany</p>
    <p class="greeting">Dear sir,</p>
    <p class="body">Communication is a very integral part of living creatures, animals and humans. Communication may be verbal or written. Written communication however is only applicable to human beings. Can you even imagine a world without communication? Verbal communication can be through telephones, webcams or in person. Written communication is through letters, emails and mobile phone messages.</p>
    <p class="body">In today's world of great inventions and technology, letters have somehow become redundant. It is the time for text messages or chats. But they still can communicate a lot more than all other modes of communication. Organizations and various government departments still bank on letters as a strong medium of communication. There is no comparison in costs of sending letters as compared to costs of mobile phone messages though – letters are far cheaper. Letters now commonly known as "hard copy documents" are considered more relevant and important than email copies of text messages as proof or evidence of some sort.</p>
    <p class="body">Letters speak volumes about a person or an organization that writes it. So one must take utmost care ensuring that the language used in any letter is appropriate for the occasion for which it is being written. Since a letter is also a written proof or document, if there are certain things that should not form a part of it, then that too should be carefully handled.</p>
    <p class="body">Writing a good letter is an art. But if for some reason someone is unable to write that perfect letter, these different types of letters provide a base for you to build on. Sample letters have been given for everyone to understand what all information needs to form a part of the letter type and then it can be customized.</p>
    <p class="closing">Yours Sincerely,<br><b>Nora Velling</b></p>
  </div>
  <div class="signature" role="img" aria-label="Handwritten signature"></div>
  <p class="disclosure">Securities and advisory services offered through Valdimo Advisor Networks LLC, member QUBEX/DLWT.<br>Valdimo is under seperate ownership from any other named entity.</p>
  <div class="band"></div>
</section>

<section class="sheet card card-front" aria-label="Business card front">
  <div class="brand"><span class="brand-dot"></span><span class="brand-name">Marlow T. Hale<br>Financial Group, LLC<small>Steady Ground For Tomorrow</small></span></div>
  <div class="person"><strong>EVAN COLTER</strong>, MPA, RFS<br>Senior Advisor<br>Portfolio Strategy and Planning</div>
  <p class="card-line" style="top:76px">4820 Harbor Avenue, Suite 310, Alder, WA 98110 · T: 555.214.3380</p>
  <p class="card-line" style="top:82px">F: 555.214.3391 · E: mhale@marlowhale.com · W: www.marlowhale.com</p>
  <div class="band"></div>
</section>

<section class="sheet card card-back" aria-label="Business card back">
  <div class="brand"><span class="brand-dot"></span><span class="brand-name">Marlow T. Hale<br>Financial Group, LLC<small>Steady Ground For Tomorrow</small></span></div>
  <p class="disclosure">Securities and advisory services offered through<br>Valdimo Advisor Networks LLC, member QUBEX/DLWT.<br>Valdimo is under seperate ownership from any other named entity.</p>
  <div class="band"></div>
</section>

<section class="sheet folder" aria-label="Presentation folder">
  <div class="folder-top"></div>
  <div class="folder-stripe"></div>
  <div class="folder-bottom"></div>
  <span class="spine" style="left:22px"></span>
  <span class="spine" style="left:29px"></span>
  <div class="brand"><span class="brand-dot"></span><span class="brand-name">Marlow T. Hale<br>Financial Group, LLC<small>Steady Ground For Tomorrow</small></span></div>
</section>

<section class="sheet envelope" aria-label="Envelope">
  <div class="brand"><span class="brand-dot"></span><span class="brand-name">Marlow T. Hale<br>Financial Group, LLC<small>Steady Ground For Tomorrow</small></span></div>
  <p class="return-addr">4820 Harbor Avenue, Suite 310<br>Alder, WA 98110</p>
  <div class="band"></div>
</section>

</body>
</html>
```